Cover for Where the Quiet River Bends Beyond Our Morning

Cover for a book that describes everything that happens to a person, from pre-birth life plans through growing in compassion and wisdom to death and living in the afterlife. The information is revealed in messages from people living in the life after this life. The title is Lanterns Along the Hidden Stair of Every Soul: Gathered from Voices Dwelling in the Further Meadow. Author is T. Morven Ashdale. Book size is 6 by 9.

Target Market(s)

General

Font styles to use
Serif

```html
<!DOCTYPE html>
<html lang="en">
<head>
<meta charset="utf-8">
<title>Lanterns Along the Hidden Stair of Every Soul — T. Morven Ashdale</title>
<link rel="stylesheet" href="https://fonts.googleapis.com/css2?family=Noto+Serif:wght@700&family=Indie+Flower&display=swap">
<style>
  :root {
    --sky-top: #0d1c44;
    --sky-mid: #23478f;
    --sky-low: #5a5f98;
    --ground: #040407;
    --window-warm: #c98a6a;
    --window-rose: #93557f;
    --window-deep: #3a2a40;
    --ink: #ffffff;
  }
  html, body {
    margin: 0;
    padding: 0;
    width: 800px;
    height: 1200px;
    overflow: hidden;
    background: var(--ground);
  }
  .cover {
    position: relative;
    width: 800px;
    height: 1200px;
    overflow: hidden;
  }
  .backdrop {
    position: absolute;
    inset: 0;
    background: linear-gradient(180deg, var(--sky-top) 0%, var(--sky-mid) 45%, var(--sky-low) 72%, #2a2540 84%, var(--ground) 94%);
  }
  .art {
    position: absolute;
    inset: 0;
  }
  .title {
    position: absolute;
    top: 80px;
    left: 36px;
    right: 36px;
    margin: 0;
    text-align: center;
    color: var(--ink);
    font-family: "Noto Serif", serif;
    font-weight: 700;
    font-size: 42px;
    line-height: 54px;
    letter-spacing: 0.14em;
    text-transform: uppercase;
  }
  .title-sub {
    display: block;
    margin-top: 8px;
    font-family: "Indie Flower", cursive;
    font-weight: 400;
    font-size: 46px;
    line-height: 54px;
    letter-spacing: 0.02em;
    text-transform: none;
  }
  .author {
    position: absolute;
    left: 0;
    right: 0;
    top: 1040px;
    margin: 0;
    text-align: center;
    color: var(--ink);
    font-family: "Indie Flower", cursive;
    font-size: 58px;
    letter-spacing: 0.02em;
  }
</style>
</head>
<body>
<main class="cover">
  <div class="backdrop" role="img" aria-label="Photograph: starry night sky above a dark hill silhouette"></div>

  <svg class="art" width="800" height="1200" viewBox="0 0 800 1200">
    <defs>
      <linearGradient id="window-fill" x1="0.2" y1="0" x2="0.6" y2="1">
        <stop offset="0" stop-color="var(--window-deep)"/>
        <stop offset="0.45" stop-color="var(--window-rose)"/>
        <stop offset="1" stop-color="var(--window-warm)"/>
      </linearGradient>
      <clipPath id="window-clip">
        <circle cx="393" cy="717" r="273"/>
      </clipPath>
    </defs>

    <circle class="photo-window" cx="393" cy="717" r="273" fill="url(#window-fill)"
            role="img" aria-label="Photograph: Milky Way over a lone figure standing on a hilltop"/>
    <polygon class="window-veil" clip-path="url(#window-clip)"
             points="1116,0 0,1116 800,1200 800,0"
             fill="#ffffff" fill-opacity="0.16"/>

    <g class="diagonal-rule" stroke="var(--ink)" stroke-width="7">
      <line x1="0" y1="894" x2="123" y2="771"/>
      <line x1="507" y1="801" x2="800" y2="504"/>
    </g>
  </svg>

  <h1 class="title">Lanterns Along the Hidden Stair of Every Soul:<span class="title-sub">Gathered from Voices Dwelling in the Further Meadow</span></h1>

  <p class="author">Written by T. Morven Ashdale</p>
</main>
</body>
</html>
```